Restaurant service company needs a website!

I am looking for a skilled web designer/developer to create a professional, responsive, and easy-to-navigate website for my company, which specializes in servicing restaurant cooking equipment. The site should communicate trust, reliability, and technical expertise to our target audience, restaurant owners, managers, and commercial kitchen operators. I have included the company logos, if any other format for them is needed please let me know.

Target Market(s)

restaurant owners, managers, and commercial kitchen operators

Industry/Entity Type

Commercial Kitchen Equipment Service

Coding

Coded - Design and coding required

Number of Pages Required

1 page

Font styles to use
Serif
Sans Serif

Requirements
Must have
• Contact and service request forms, Click-to-call functionality for mobile, Clean, modern layout with strong visuals, Easy navigation, mobile-friendly
Nice to have
• Testimonials or Reviews, If possible a click-to-text functionality for mobile.
Should not have
• Any mention of Refrigeration or HVAC, "Free Quotes"

```html
<!DOCTYPE html>
<html lang="en">
<head>
<meta charset="utf-8">
<title>Ridgeline Kitchen Service</title>
<link rel="stylesheet" href="https://fonts.googleapis.com/css2?family=Kanit:wght@300;400;600;700&family=Inter:wght@400;500;600;700&display=swap">
<style>
:root{
  --teal:#0b5f78;
  --teal-dark:#084a5e;
  --teal-light:#d8ecf3;
  --ink:#1d1d1f;
  --muted:#555b60;
  --line:#d9dde0;
  --paper:#ffffff;
  --mist:#f4f5f6;
  --night:#141a1d;
}
*{box-sizing:border-box;margin:0;padding:0}
html,body{width:1200px;height:4205px;overflow:hidden}
body{font-family:"Inter",Arial,sans-serif;color:var(--ink);background:var(--paper);position:relative}
.abs{position:absolute}
.display{font-family:"Kanit",Arial,sans-serif;font-weight:300;text-transform:uppercase;letter-spacing:1px;line-height:1.15}
.display b{font-weight:600}
.btn{display:inline-flex;align-items:center;gap:8px;height:38px;padding:0 20px 0 10px;border-radius:19px;font-size:13px;font-weight:500;text-decoration:none}
.btn .dot{width:20px;height:20px;border-radius:50%;border:3px solid var(--teal-light)}
.btn-teal{background:var(--teal);color:#fff}
.btn-white{background:#fff;color:var(--teal)}
.btn-outline{border:1.5px solid var(--teal);color:var(--teal);background:#fff}
.label{font-size:13px;font-weight:600;color:var(--teal)}
.pill{display:inline-block;background:#9fbfca;color:var(--teal-dark);font-size:12px;font-weight:600;padding:3px 14px;border-radius:10px}

/* header */
.site-header{left:0;top:0;width:1200px;height:68px;background:#fff}
.brand{display:flex;align-items:center;gap:8px;font-family:"Inter",sans-serif;font-weight:700;font-size:18px;color:var(--teal);letter-spacing:.5px}
.brand .mark{width:16px;height:16px;background:var(--teal)}
.nav{display:flex;gap:32px;font-size:13px;color:var(--ink)}

/* hero */
.hero{left:0;top:68px;width:1200px;height:590px;background:radial-gradient(ellipse at 50% 30%,#6d7478 0%,#3a4043 45%,#1b1f21 100%)}
.hero h1{color:#fff;font-size:50px;text-align:center;width:1200px}

/* about */
.about p{font-size:12.5px;line-height:21px;color:var(--muted)}

/* services */
.services{left:0;top:1100px;width:1200px;height:748px;background:linear-gradient(180deg,#24687d 0%,#1c5669 60%,#164657 100%)}
.svc-card{width:213px;text-align:center;color:#fff}
.svc-photo{height:237px;border:2px solid #fff;background:linear-gradient(160deg,#8a949a,#4b5559)}
.svc-icon{width:72px;height:72px;border-radius:50%;background:var(--teal);border:4px solid #fff;margin:-38px auto 0;display:flex;align-items:center;justify-content:center;position:relative}
.svc-card h3{font-size:21px;font-weight:600;line-height:23px;margin-top:12px}
.svc-card p{font-size:12px;line-height:17px;color:#d3e2e7;margin-top:8px;padding:0 6px}

/* trusted */
.trusted{left:0;top:1848px;width:1200px;height:652px;background:var(--mist)}
.feature{display:flex;gap:12px}
.feature h4{font-size:13.5px;font-weight:600}
.feature p{font-size:12.5px;color:var(--muted);margin-top:8px}

/* testimonials */
.quote-card{width:294px;height:218px;border:1.5px solid var(--line);border-radius:8px;background:#fff;padding:28px 24px}
.quote-card p{font-size:12.5px;line-height:21px;color:var(--muted)}
.person{display:flex;align-items:center;gap:10px;position:absolute;left:24px;bottom:24px}
.avatar{width:44px;height:44px;border-radius:50%;background:linear-gradient(135deg,#c9cdd0,#7d868b)}
.person strong{font-size:13.5px;display:block}
.person span{font-size:11px;color:var(--muted)}

/* contact */
.contact-band{left:0;top:3075px;width:1200px;height:477px;background:linear-gradient(180deg,#1c6a82,#185b70)}
.contact-dark{left:0;top:3552px;width:1200px;height:188px;background:var(--night)}
.panel{left:137px;top:3292px;width:925px;height:446px;background:#fff}
.panel-side{left:0;top:0;width:291px;height:446px;background:var(--teal);color:#fff;padding:0 38px}
.side-h{font-size:13px;display:flex;align-items:center;gap:8px;letter-spacing:.5px}
.side-ic{width:16px;height:16px;border-radius:50%;background:#fff}
.field label{font-size:12.5px;font-weight:600;display:block;margin-bottom:10px}
.field label i{color:#d12b2b;font-style:normal}
.input{height:40px;border:1.5px solid var(--line);border-radius:6px;font-size:12px;color:#8b9196;padding:12px 14px}

/* footer */
.footer h5{font-size:14px;font-weight:600;letter-spacing:1px}
.footer li{list-style:none;font-size:12.5px;color:var(--ink);margin-top:18px}
.social{width:28px;height:28px;border-radius:50%;border:1.5px solid #555}
</style>
</head>
<body>

<header class="site-header abs">
  <div class="brand abs" style="left:90px;top:22px"><span class="mark"></span>RIDGELINE</div>
  <nav class="nav abs" style="left:502px;top:26px"><span>Home</span><span>Services</span><span>About Us</span><span>Testimonials</span><span>Contact</span></nav>
  <a class="btn btn-teal abs" style="left:925px;top:15px" href="#request"><span class="dot"></span>Request Service »</a>
</header>

<section class="hero abs" role="img" aria-label="Photo of a stainless steel commercial restaurant kitchen">
  <h1 class="display abs" style="top:225px">Professional <b>Kitchen<br>Equipment</b> Service for<br><b>Restaurants.</b></h1>
  <p class="abs" style="top:420px;width:1200px;text-align:center;color:#fff;font-size:13px;font-weight:600">Fast, reliable, and expert maintenance to keep your kitchen running without interruption.</p>
  <a class="btn btn-teal abs" style="left:434px;top:471px" href="#request"><span class="dot"></span>Request Service »</a>
  <a class="btn btn-white abs" style="left:624px;top:471px" href="tel:+12175550142"><span class="dot"></span>Call Us Now »</a>
</section>

<section class="about">
  <div class="label abs" style="left:164px;top:735px">About Us</div>
  <h2 class="display abs" style="left:164px;top:756px;font-size:40px">Who <b>we</b> are</h2>
  <p class="abs" style="left:164px;top:820px;width:350px;font-weight:500;color:var(--ink)">We are a dedicated team of certified service engineers with years of experience in the HoReCa industry.</p>
  <a class="btn btn-outline abs" style="left:164px;top:894px" href="#about"><span class="dot"></span>Read More About Us »</a>
  <p class="abs" style="left:600px;top:762px;width:436px">Our expertise covers all major types of commercial kitchen equipment, from ovens and ranges to specialized cooking systems.We understand the pressure restaurant owners, managers, and chefs face every day, and our goal is to provide fast, reliable, and professional support that keeps your kitchen fully operational.</p>
  <p class="abs" style="left:600px;top:888px;width:436px">What sets us apart is our focus on trust and long-term relationships. We don't just fix equipment — we help prevent breakdowns, reduce costs, and extend the lifespan of your investment. With transparent communication, high-quality standards, and a customer-first approach, we ensure that every client receives dependable service and peace of mind.</p>
</section>

<section class="services abs" role="img" aria-label="Background photo of a commercial kitchen with teal tint">
  <div class="abs" style="left:0;top:44px;width:1200px;text-align:center"><span class="pill">Services</span></div>
  <h2 class="display abs" style="left:0;top:72px;width:1200px;text-align:center;color:#fff;font-size:42px;line-height:56px">Comprehensive <b>Service</b><br>for <b>Commercial Kitchen</b><br>Equipment</h2>
  <p class="abs" style="left:0;top:260px;width:1200px;text-align:center;color:#fff;font-size:13px;font-weight:600">We help restaurant owners, managers, and chefs keep their kitchens operating at peak performance.</p>

  <div class="svc-card abs" style="left:137px;top:312px">
    <div class="svc-photo" role="img" aria-label="Technician writing a repair report"></div>
    <div class="svc-icon"><svg width="32" height="32" viewBox="0 0 32 32" fill="none" stroke="#fff" stroke-width="2"><rect x="7" y="5" width="18" height="23" rx="2"/><path d="M11 12h10M11 17h10M11 22h6"/></svg></div>
    <h3>Diagnostics &amp;<br>Repairs</h3><p>Quick identification and resolution of equipment issues.</p>
  </div>
  <div class="svc-card abs" style="left:375px;top:312px">
    <div class="svc-photo" role="img" aria-label="Engineer inspecting a kitchen exhaust hood"></div>
    <div class="svc-icon"><svg width="32" height="32" viewBox="0 0 32 32" fill="none" stroke="#fff" stroke-width="2.4"><circle cx="16" cy="16" r="6"/><path d="M16 4v5M16 23v5M4 16h5M23 16h5M8 8l3 3M21 21l3 3M24 8l-3 3M11 21l-3 3"/></svg></div>
    <h3>Preventive<br>Maintenance</h3><p>Regular check-ups to avoid unexpected breakdowns.</p>
  </div>
  <div class="svc-card abs" style="left:613px;top:312px">
    <div class="svc-photo" role="img" aria-label="Technician repairing an appliance on site"></div>
    <div class="svc-icon"><svg width="32" height="32" viewBox="0 0 32 32" fill="none" stroke="#fff" stroke-width="2.4"><circle cx="16" cy="17" r="10"/><path d="M16 11v6l4 3M13 4h6"/></svg></div>
    <h3>Emergency<br>Service</h3><p>On-site support whenever you need it most.</p>
  </div>
  <div class="svc-card abs" style="left:850px;top:312px">
    <div class="svc-photo" role="img" aria-label="Clean commercial range line under a hood"></div>
    <div class="svc-icon"><svg width="32" height="32" viewBox="0 0 32 32" fill="none" stroke="#fff" stroke-width="2.6"><circle cx="16" cy="16" r="11"/><path d="M11 16l4 4 7-8"/></svg></div>
    <h3>Quality<br>Guarantee</h3><p>Genuine parts and professional workmanship.</p>
  </div>
</section>
<div class="abs" style="left:10px;top:1005px;width:210px;height:210px;border-radius:50%;background:#fff"></div>
<div class="abs" style="left:20px;top:1015px;width:170px;height:170px;border-radius:50%;background:var(--teal-light)"></div>

<section class="trusted abs">
  <div class="abs" style="left:137px;top:96px;width:448px;height:556px;background:linear-gradient(160deg,#9aa3a8,#4a5357)" role="img" aria-label="Smiling technician in a cap holding pliers"></div>
  <div class="abs" style="left:433px;top:152px;width:629px;height:195px;background:#fff"></div>
  <h2 class="display abs" style="left:468px;top:176px;font-size:42px;line-height:48px">Trusted by <b>Restaurants</b><br>and <b>Kitchens</b> across<br>the city</h2>
  <p class="abs" style="left:655px;top:348px;width:340px;font-size:12.5px;line-height:21px;font-weight:600;color:#333">Our reputation is built on expertise, transparency, and fast response times.</p>
  <div class="feature abs" style="left:652px;top:416px"><svg width="28" height="28" viewBox="0 0 28 28" fill="none" stroke="var(--teal)" stroke-width="2"><circle cx="14" cy="10" r="6"/><path d="M4 26c1-6 5-9 10-9s9 3 10 9"/></svg><div><h4>Experienced Engineers</h4><p>years of hands-on industry knowledge</p></div></div>
  <div class="feature abs" style="left:652px;top:482px"><svg width="28" height="28" viewBox="0 0 28 28" fill="none" stroke="var(--teal)" stroke-width="2"><circle cx="17" cy="15" r="8"/><path d="M17 10v5l3 2M2 12h6M3 17h5"/></svg><div><h4>Speed &amp; Reliability</h4><p>minimizing downtime for your business.</p></div></div>
  <div class="feature abs" style="left:652px;top:548px"><svg width="28" height="28" viewBox="0 0 28 28" fill="none" stroke="var(--teal)" stroke-width="2"><path d="M5 16v-3a9 9 0 0118 0v3"/><rect x="3" y="15" width="5" height="8" rx="2"/><rect x="20" y="15" width="5" height="8" rx="2"/></svg><div><h4>24/7 Support</h4><p>always available when your kitchen needs us.</p></div></div>
  <div class="abs" style="left:1005px;top:505px;width:195px;height:195px;border-radius:50%;background:var(--teal-light);opacity:.7"></div>
</section>

<section class="testimonials">
  <div class="label abs" style="left:0;top:2583px;width:1200px;text-align:center">Testimonials</div>
  <h2 class="display abs" style="left:0;top:2602px;width:1200px;text-align:center;font-size:40px">What our <b>clients</b> say</h2>
  <div class="quote-card abs" style="left:137px;top:2700px"><p>"Thanks to this team, our kitchen downtime has been reduced to a minimum. Fast, professional, and always available."</p><div class="person"><div class="avatar" role="img" aria-label="Client portrait"></div><div><strong>Marcus</strong><span>Owner of Bistro Nine</span></div></div></div>
  <div class="quote-card abs" style="left:453px;top:2700px"><p>"Their preventive maintenance service helps us run smoothly without unexpected issues. Highly recommended."</p><div class="person"><div class="avatar" role="img" aria-label="Client portrait"></div><div><strong>Lena</strong><span>Head Chef at Oak Street Grill</span></div></div></div>
  <div class="quote-card abs" style="left:768px;top:2700px"><p>"Thanks to this team, our kitchen downtime has been reduced to a minimum. Fast, professional, and always available."</p><div class="person"><div class="avatar" role="img" aria-label="Client portrait"></div><div><strong>Marcus</strong><span>Owner of Bistro Nine</span></div></div></div>
  <svg class="abs" style="left:172px;top:2686px" width="24" height="18" viewBox="0 0 24 18" fill="var(--teal)"><path d="M0 18V9C0 4 3 1 8 0v4C5 5 4 7 4 9h6v9zM13 18V9c0-5 3-8 8-9v4c-3 1-4 3-4 5h6v9z"/></svg>
  <svg class="abs" style="left:488px;top:2686px" width="24" height="18" viewBox="0 0 24 18" fill="var(--teal)"><path d="M0 18V9C0 4 3 1 8 0v4C5 5 4 7 4 9h6v9zM13 18V9c0-5 3-8 8-9v4c-3 1-4 3-4 5h6v9z"/></svg>
  <svg class="abs" style="left:803px;top:2686px" width="24" height="18" viewBox="0 0 24 18" fill="var(--teal)"><path d="M0 18V9C0 4 3 1 8 0v4C5 5 4 7 4 9h6v9zM13 18V9c0-5 3-8 8-9v4c-3 1-4 3-4 5h6v9z"/></svg>
  <div class="abs" style="left:137px;top:2968px;width:830px;height:1px;background:var(--line)"></div>
  <div class="abs" style="left:137px;top:2967px;width:205px;height:3px;background:var(--teal)"></div>
  <div class="abs" style="left:988px;top:2952px;width:32px;height:32px;border:1px solid #aaa;border-radius:4px;display:flex;align-items:center;justify-content:center;font-size:16px">‹</div>
  <div class="abs" style="left:1030px;top:2952px;width:32px;height:32px;background:var(--teal);color:#fff;border-radius:4px;display:flex;align-items:center;justify-content:center;font-size:16px">›</div>
</section>

<section class="contact" id="request">
  <div class="contact-band abs" role="img" aria-label="Teal tinted kitchen background photo"></div>
  <div class="contact-dark abs"></div>
  <div class="abs" style="left:0;top:3137px;width:1200px;text-align:center"><span class="pill">Contact Us</span></div>
  <h2 class="display abs" style="left:0;top:3160px;width:1200px;text-align:center;color:#fff;font-size:42px">Need help <b>right away</b>?</h2>
  <p class="abs" style="left:0;top:3223px;width:1200px;text-align:center;color:#fff;font-size:12.5px;line-height:21px;font-weight:600">Request service or call us now – a technician will be on-site<br>as soon as possible.</p>

  <div class="panel abs">
    <div class="panel-side abs">
      <h3 class="abs" style="left:38px;top:94px;font-size:22px;font-weight:600;letter-spacing:1px">GET IN TOUCH</h3>
      <div class="side-h abs" style="left:38px;top:148px"><span class="side-ic"></span>LOCATION</div>
      <p class="abs" style="left:38px;top:180px;font-size:12px;line-height:21px"><b>Ridgeline Kitchen Service Inc.</b><br>&nbsp;118 Harbor Lane, Suite 400<br>&nbsp;Springfield, IL 62701, USA</p>
      <div class="side-h abs" style="left:38px;top:262px"><span class="side-ic"></span>EMAIL</div>
      <p class="abs" style="left:38px;top:292px;font-size:12px">hello@ridgelinekitchen.example</p>
      <div class="side-h abs" style="left:38px;top:334px"><span class="side-ic"></span>PHONE</div>
      <p class="abs" style="left:38px;top:364px;font-size:12px;line-height:21px">+1 (217) 555-0142<br>+1 (217) 555-0178</p>
    </div>
    <div class="field abs" style="left:323px;top:56px;width:275px"><label>Full Name <i>*</i></label><div class="input" style="border-color:var(--teal)">Enter Your Name</div></div>
    <div class="field abs" style="left:610px;top:56px;width:275px"><label>Company <i>*</i></label><div class="input">Enter Your Company</div></div>
    <div class="field abs" style="left:323px;top:141px;width:275px"><label>Email <i>*</i></label><div class="input">Enter Your Email</div></div>
    <div class="field abs" style="left:610px;top:141px;width:275px"><label>Work Phone <i>*</i></label><div class="input">Enter Your Phone</div></div>
    <div class="field abs" style="left:323px;top:226px;width:562px"><label>Message</label><div class="input" style="height:100px">Enter Your Message</div></div>
    <a class="btn btn-teal abs" style="left:742px;top:354px" href="#submit"><span class="dot"></span>Submit Now »</a>
  </div>
  <div class="abs" style="left:128px;top:3274px;width:82px;height:82px;border-radius:50%;background:#fff"></div>
  <div class="abs" style="left:140px;top:3286px;width:58px;height:58px;border-radius:50%;background:var(--teal-light)"></div>
</section>

<footer class="footer">
  <div class="abs" style="left:210px;top:3795px;width:60px;height:60px;background:var(--teal)"></div>
  <div class="abs" style="left:160px;top:3906px;width:245px;text-align:center;font-weight:700;font-size:20px;color:var(--teal);letter-spacing:1px">RIDGELINE</div>
  <div class="abs" style="left:160px;top:3934px;width:245px;text-align:center;font-size:10px;color:var(--teal);letter-spacing:4px">KITCHEN SERVICE</div>
  <div class="social abs" style="left:221px;top:3968px"></div>
  <div class="social abs" style="left:268px;top:3968px"></div>
  <div class="social abs" style="left:316px;top:3968px"></div>

  <div class="abs" style="left:428px;top:3805px"><h5>QUICK LINKS</h5><ul><li>Services</li><li>About</li><li>Testimonials</li><li>Request Service</li><li>Contact</li></ul></div>
  <div class="abs" style="left:580px;top:3800px;width:1px;height:270px;background:var(--line)"></div>
  <div class="abs" style="left:624px;top:3805px"><h5>SERVICES</h5><ul><li>Diagnostics &amp; Repairs</li><li>Preventive Maintenance</li><li>Emergency Service</li><li>Quality Guarantee</li></ul></div>
  <div class="abs" style="left:815px;top:3805px;font-size:12px;line-height:20px"><h5>CONTACT</h5>
    <p style="margin-top:16px;padding-left:28px">118 Harbor Lane, Suite 400<br>Springfield, IL 62701, USA</p>
    <p style="margin-top:14px;padding-left:28px">hello@ridgelinekitchen.example</p>
    <p style="margin-top:14px;padding-left:28px">+1 (217) 555-0142<br>+1 (217) 555-0178</p>
  </div>
  <svg class="abs" style="left:815px;top:3845px" width="14" height="16" viewBox="0 0 14 16" fill="none" stroke="var(--teal)" stroke-width="1.6"><path d="M7 15s5-5 5-9a5 5 0 00-10 0c0 4 5 9 5 9z"/><circle cx="7" cy="6" r="2"/></svg>
  <svg class="abs" style="left:815px;top:3898px" width="14" height="11" viewBox="0 0 14 11" fill="none" stroke="var(--teal)" stroke-width="1.4"><rect x="1" y="1" width="12" height="9"/><path d="M1 1l6 5 6-5"/></svg>
  <svg class="abs" style="left:815px;top:3932px" width="14" height="14" viewBox="0 0 14 14" fill="var(--teal)"><path d="M3 1l3 3-2 2c1 2 2 3 4 4l2-2 3 3-2 2C6 13 1 8 1 3z"/></svg>
  <div class="abs" style="left:580px;top:4014px;width:482px;height:1px;background:var(--line)"></div>
  <h5 class="abs" style="left:624px;top:4037px">SUBSCRIBE OUR NEWSLETTER</h5>
  <div class="abs" style="left:624px;top:4068px;width:296px;height:36px;border:1.5px solid var(--line);border-radius:18px;font-size:12px;color:#8b9196;padding:10px 20px">Enter your email address...</div>
  <a class="btn btn-teal abs" style="left:928px;top:4068px;height:36px" href="#subscribe"><span class="dot"></span>Subscribe »</a>
  <div class="abs" style="left:137px;top:4158px;width:925px;height:1px;background:var(--line)"></div>
  <p class="abs" style="left:137px;top:4174px;font-size:11px;color:var(--muted)">© 2025 Ridgeline Kitchen Service. All rights reserved.</p>
  <p class="abs" style="left:870px;top:4174px;font-size:11px;color:var(--muted)">Privacy Policy</p>
  <p class="abs" style="left:975px;top:4174px;font-size:11px;color:var(--muted)">Terms of Service</p>
</footer>

</body>
</html>
```